Business Cards for a law firm

Business cards for our law firm. Use our silhoette logo and OAK HARBOR - check our website (www.oakharbor-legal.com)

Contact Information for Business Card

our silhouette logo, OAK HARBOR, 800-555-0147, Dorian Kestrup, dorian@oakharbor-legal.com

Requirements
Must have
• our silhouette logo, OAK HARBOR, 800-555-0147, Dorian Kestrup, dorian@oakharbor-legal.com

```html
<!DOCTYPE html>
<html lang="en">
<head>
<meta charset="utf-8">
<title>Oak Harbor – Business Cards</title>
<link rel="stylesheet" href="https://fonts.googleapis.com/css2?family=Cinzel:wght@700&family=Questrial&display=swap">
<style>
  :root {
    --backdrop: #6e6e6e;
    --card-navy: #23336b;
    --card-navy-light: #27387a;
    --emboss-navy: #1c2a5c;
    --ink-white: #ffffff;
  }
  * { margin: 0; padding: 0; box-sizing: border-box; }
  html, body { width: 900px; height: 1200px; overflow: hidden; }
  body { background: var(--backdrop); position: relative; font-family: "Questrial", sans-serif; }

  .card {
    position: absolute;
    left: 134px;
    width: 632px;
    height: 364px;
    background: linear-gradient(135deg, var(--card-navy) 0%, var(--card-navy-light) 100%);
    color: var(--ink-white);
  }
  .card--front { top: 210px; }
  .card--back { top: 624px; }

  .brand {
    position: absolute;
    left: 60px;
    display: flex;
    align-items: center;
    gap: 22px;
  }
  .card--front .brand { top: 118px; color: var(--emboss-navy); }
  .card--back .brand { top: 120px; color: var(--ink-white); }
  .brand__mark { width: 44px; height: 44px; background: currentColor; }
  .brand__name {
    font-family: "Cinzel", serif;
    font-weight: 700;
    font-size: 50px;
    letter-spacing: 1px;
    line-height: 1;
  }

  .front-url {
    position: absolute;
    top: 318px;
    left: 0; right: 0;
    text-align: center;
    font-size: 12px;
    letter-spacing: 3.4px;
    text-transform: uppercase;
  }

  .person {
    position: absolute;
    top: 250px;
    right: 340px;
    text-align: right;
    text-transform: uppercase;
  }
  .person__name { font-size: 19px; letter-spacing: 0.8px; font-weight: 700; }
  .person__role { font-size: 14px; letter-spacing: 0.8px; margin-top: 6px; }

  .divider {
    position: absolute;
    left: 316px; top: 238px;
    width: 2px; height: 70px;
    background: var(--ink-white);
  }

  .contacts {
    position: absolute;
    left: 336px; top: 238px;
    list-style: none;
    text-transform: uppercase;
  }
  .contacts li {
    display: flex; align-items: center; gap: 6px;
    height: 27px;
    font-size: 12.5px; letter-spacing: 0.6px;
  }
  .contacts li.contacts__phone { font-size: 15px; letter-spacing: 2px; }
  .contacts svg { width: 13px; height: 13px; fill: var(--ink-white); flex: none; }
</style>
</head>
<body>
  <section class="card card--front" aria-label="Card front">
    <div class="brand">
      <span class="brand__mark"></span>
      <span class="brand__name">OAK HARBOR</span>
    </div>
    <p class="front-url">www.oakharbor-legal.com</p>
  </section>

  <section class="card card--back" aria-label="Card back">
    <div class="brand">
      <span class="brand__mark"></span>
      <span class="brand__name">OAK HARBOR</span>
    </div>
    <div class="person">
      <p class="person__name">Dorian Kestrup</p>
      <p class="person__role">Attorney</p>
    </div>
    <span class="divider"></span>
    <ul class="contacts">
      <li class="contacts__phone">
        <svg viewBox="0 0 24 24"><path d="M6.6 10.8a15.1 15.1 0 0 0 6.6 6.6l2.2-2.2a1 1 0 0 1 1-.25 11.4 11.4 0 0 0 3.6.57 1 1 0 0 1 1 1V20a1 1 0 0 1-1 1A17 17 0 0 1 3 4a1 1 0 0 1 1-1h3.5a1 1 0 0 1 1 1c0 1.25.2 2.45.57 3.57a1 1 0 0 1-.25 1z"/></svg>
        800-555-0147
      </li>
      <li>
        <svg viewBox="0 0 24 24"><path d="M2 5h20v14H2z M3.5 6.5l8.5 6.5 8.5-6.5" fill="none" stroke="#fff" stroke-width="2"/><path d="M2 5h20L12 12z"/></svg>
        dorian@oakharbor-legal.com
      </li>
      <li>
        <svg viewBox="0 0 24 24"><circle cx="12" cy="12" r="9" fill="none" stroke="#fff" stroke-width="2"/><path d="M3 12h18M12 3c3 3 3 15 0 18M12 3c-3 3-3 15 0 18" fill="none" stroke="#fff" stroke-width="1.6"/></svg>
        www.oakharbor-legal.com
      </li>
    </ul>
  </section>
</body>
</html>
```